Flyer Design

we need a flyer design for a new company Thistlecombe Garden maintenance
we want a leaflet for our gardening services.
we do lawn cutting,hedge cutting, lawn treatments,tree work, full garden maintenance.
I have attached some ones i like so this might give you a starting point.

Industry/Entity Type

It Company

```html
<!DOCTYPE html>
<html lang="en">
<head>
<meta charset="utf-8">
<title>Thistlecombe Garden maintenance – Flyers</title>
<link href="https://fonts.googleapis.com/css2?family=Oswald:wght@400;500;600;700&display=swap" rel="stylesheet">
<style>
  :root{
    --bg:#2a2a2a;
    --blue:#1533a8;
    --blue-light:#8ea3dc;
    --panel:#eef0f2;
    --ink:#222;
    --ink-soft:#333;
    --white:#fff;
    --garden-sky:#9cc6e8;
    --garden-green:#4f8a2e;
    --garden-deep:#2f5a1c;
  }
  *{margin:0;padding:0;box-sizing:border-box}
  html,body{width:900px;height:1200px;overflow:hidden;background:var(--bg)}
  body{position:relative;font-family:"Oswald",sans-serif}
  .flyer{position:absolute;width:795px;height:558px;overflow:hidden;background:var(--white)}
  .flyer--front{left:53px;top:25px}
  .flyer--back{left:55px;top:617px}
  .flyer svg.shapes{position:absolute;inset:0}
  .photo{position:absolute}
  .brand{position:absolute;display:flex;align-items:center;gap:10px}
  .brand__mark{width:22px;height:22px;background:var(--blue)}
  .brand__name{font-weight:700;font-size:32px;color:var(--ink);letter-spacing:.5px;line-height:1}
  .services-title{position:absolute;left:548px;top:232px;width:247px;height:44px;
    background:rgba(200,210,235,.55);color:var(--blue);font-weight:500;font-size:30px;
    text-align:right;padding-right:24px;line-height:44px}
  .services-list{position:absolute;right:25px;top:292px;list-style:none;text-align:right}
  .services-list li{font-weight:500;font-size:23px;color:var(--ink-soft);line-height:40px}
  .call-band{position:absolute;height:43px;background:var(--blue);color:var(--white);
    display:flex;align-items:center;gap:14px;font-weight:500;font-size:26px;letter-spacing:.5px}
  .call-band svg{width:30px;height:30px}
  .flyer--front .call-band{left:0;top:507px;width:540px;padding-left:44px}
  .flyer--back .call-band{left:395px;top:505px;width:400px;padding-left:10px}
  .headline{position:absolute;left:345px;top:33px;width:450px;height:42px;background:var(--blue);
    color:var(--white);font-weight:600;font-size:29px;line-height:42px;padding-left:14px}
  .services-intro{position:absolute;left:360px;top:86px;color:var(--white);font-weight:500;font-size:25px}
  .garden-list{position:absolute;left:360px;top:128px;list-style:none}
  .garden-list li{display:flex;align-items:center;gap:10px;color:var(--white);font-weight:500;font-size:21px;line-height:33px}
  .garden-list li::before{content:"";width:18px;height:18px;border-radius:50%;border:2px solid var(--white);background:rgba(255,255,255,.25)}
</style>
</head>
<body>

<section class="flyer flyer--front">
  <div class="photo" role="img" aria-label="Photo of a blue house porch with hanging flower basket, trimmed shrubs and red flower beds"
       style="left:0;top:0;width:600px;height:558px;background:linear-gradient(180deg,#5a6f8f 0%,#6d9a4a 35%,#3f7326 70%,#b93a4a 86%,#5e8f33 100%)"></div>
  <svg class="shapes" viewBox="0 0 795 558" aria-hidden="true">
    <path d="M500,0 C520,140 600,250 610,558 L795,558 L795,0 Z" fill="var(--panel)"/>
    <path d="M455,0 C470,150 560,250 545,558 L605,558 C600,260 510,150 500,0 Z" fill="var(--blue)"/>
    <path d="M500,0 C520,140 600,250 610,558 L620,558 C615,250 540,140 525,0 Z" fill="var(--white)"/>
    <path d="M525,0 C545,100 590,170 600,230 L592,230 C580,170 535,100 515,0 Z" fill="var(--blue-light)"/>
  </svg>
  <div class="brand" style="left:560px;top:104px">
    <span class="brand__mark"></span><span class="brand__name">THISTLECOMBE</span>
  </div>
  <div class="services-title">OUR SERVICES</div>
  <ul class="services-list">
    <li>LAWN CUTTING</li>
    <li>HEDGE CUTTING</li>
    <li>LAWN TREATMENTS</li>
    <li>TREE WORK</li>
    <li>FULL GARDEN</li>
    <li>MAINTENANCE</li>
  </ul>
  <div class="call-band">
    <span>CALL NOW</span>
    <svg viewBox="0 0 30 30" aria-hidden="true"><circle cx="15" cy="15" r="13" fill="none" stroke="#fff" stroke-width="2"/><path d="M10 8 l3 0 l1.5 4 l-2 1.5 a9 9 0 0 0 4 4 l1.5-2 l4 1.5 l0 3 a2 2 0 0 1-2 2 a13 13 0 0 1-12-12 a2 2 0 0 1 2-2z" fill="#fff"/></svg>
    <span>1234 567 890</span>
  </div>
</section>

<section class="flyer flyer--back">
  <div class="photo" role="img" aria-label="Photo of a petrol lawn mower on a green lawn in front of tall garden plants"
       style="left:250px;top:0;width:545px;height:558px;background:linear-gradient(180deg,#6b7f4e 0%,#3d6a26 45%,#5d9a34 100%)"></div>
  <div class="photo" role="img" aria-label="Photo of a ride-on mower cutting a wide lawn in front of a house"
       style="left:0;top:0;width:250px;height:180px;background:linear-gradient(180deg,var(--garden-sky) 0%,#c9dfe9 35%,#6aa83a 55%,var(--garden-green) 100%)"></div>
  <div class="photo" role="img" aria-label="Photo of a neatly trimmed hedge beside a lawn"
       style="left:0;top:190px;width:250px;height:205px;background:linear-gradient(180deg,#d9dcd6 0%,var(--garden-deep) 20%,#3f7a22 60%,#6fae3a 100%)"></div>
  <svg class="shapes" viewBox="0 0 795 558" aria-hidden="true">
    <path d="M0,395 L260,395 C290,450 300,500 305,558 L0,558 Z" fill="var(--white)"/>
    <path d="M225,0 L300,0 C270,120 250,250 370,558 L300,558 C190,300 200,150 225,0 Z" fill="var(--blue)"/>
    <path d="M285,0 L320,0 C290,100 290,200 350,270 L330,270 C265,200 260,100 285,0 Z" fill="var(--white)"/>
    <path d="M320,0 L360,0 C325,80 325,150 345,200 L335,200 C305,150 300,80 320,0 Z" fill="var(--blue-light)"/>
    <path d="M180,0 L225,0 C205,120 200,260 300,558 L280,558 C180,300 170,150 180,0 Z" fill="var(--white)"/>
  </svg>
  <div class="brand" style="left:36px;top:454px">
    <span class="brand__mark"></span><span class="brand__name">THISTLECOMBE</span>
  </div>
  <div class="headline">NEED HELP IN THE GARDEN?</div>
  <div class="services-intro">Our Gardening Services Include</div>
  <ul class="garden-list">
    <li>Grass Cutting</li>
    <li>Hedge Cutting</li>
    <li>Tidy Ups</li>
    <li>Weeding Tree Work</li>
    <li>Full Garden Maintenance</li>
  </ul>
  <div class="call-band">
    <span>CALL NOW</span>
    <svg viewBox="0 0 30 30" aria-hidden="true"><circle cx="15" cy="15" r="13" fill="none" stroke="#fff" stroke-width="2"/><path d="M10 8 l3 0 l1.5 4 l-2 1.5 a9 9 0 0 0 4 4 l1.5-2 l4 1.5 l0 3 a2 2 0 0 1-2 2 a13 13 0 0 1-12-12 a2 2 0 0 1 2-2z" fill="#fff"/></svg>
    <span>1234 567 890</span>
  </div>
</section>

</body>
</html>
```